Designing a brochures for an educational counseling service provider

We would like a 4 sided design on a 11x8.5 paper, half folded. I have including a sample design we did to give you an idea of what we envision but we welcome creativity to make beautiful looking flyers. Text for the flier is included as well as our logo.
- The most important thing is capturing our audience/market. We will be handing these flies to schools, organizations and individual clients.

www.plorvaeducationalconsultants.example

Target Market(s)

We are targeting international students wanting to study in the U.S and Canada.

Industry/Entity Type

Education

Requirements
Must have
• - Clean and clear
• - Our logo should visible and well placed.
• - Could you the pictures of students, libraries and school buildings or you could use the pictures we already have.
Nice to have
• We would like this to match business cards.

```html
<!DOCTYPE html>
<html lang="en">
<head>
<meta charset="utf-8">
<title>Plorva Educational Consultants – Brochure</title>
<link href="https://fonts.googleapis.com/css2?family=Arimo:ital,wght@0,400;0,700;1,400;1,700&display=swap" rel="stylesheet">
<style>
:root{
  --bg:#ececec;
  --paper:#ffffff;
  --navy:#1b2a6b;
  --blue:#1f4f9e;
  --green:#4aa04a;
  --light-green:#b9d98a;
  --ink:#1e1e1e;
  --beige:rgba(238,226,196,.85);
  --tick:#2a3f8f;
}
*{margin:0;padding:0;box-sizing:border-box}
html,body{width:1200px;height:800px;overflow:hidden;background:var(--bg)}
body{font-family:"Arimo",Arial,sans-serif;color:var(--ink);position:relative}
.page{position:absolute;top:22px;width:476px;height:756px;background:var(--paper);overflow:hidden}
.page--left{left:76px}
.page--right{left:609px}
.photo{position:absolute}

/* left page */
.who-block{position:absolute;left:0;top:0;width:107px;height:137px;
  background:linear-gradient(160deg,var(--green) 0%,var(--blue) 70%);
  color:#fff;font-style:italic;font-size:25px;line-height:30px;letter-spacing:1px;
  padding:16px 0 0 14px}
.photo--students{left:107px;top:0;width:369px;height:137px;
  background:linear-gradient(120deg,#c9a98a 0%,#6d8fae 35%,#9bb56d 60%,#d9c2a8 100%)}
.intro{position:absolute;left:36px;top:160px;width:410px;font-size:9.5px;line-height:17px}
.intro p{margin-bottom:7px}
.ticks{list-style:none;margin-top:4px}
.ticks li{position:relative;padding-left:16px;margin-bottom:8px}
.ticks svg{position:absolute;left:0;top:3px;width:10px;height:10px}
.photo--library{left:0;top:407px;width:476px;height:326px;
  background:linear-gradient(180deg,#efe8dc 0%,#c9a67a 40%,#7a4e2d 75%,#4a2f1d 100%)}
.library-banner{position:absolute;left:0;top:450px;width:476px;height:62px;background:var(--beige);
  display:flex;align-items:center;justify-content:center;text-align:center;
  font-weight:700;font-size:13.5px;line-height:18px;color:#111;padding:0 40px}
.brand{position:absolute;right:20px;top:688px;display:flex;align-items:center;gap:5px;
  font-weight:700;font-size:14px;color:var(--navy)}
.brand-dot{width:14px;height:14px;border-radius:50%;background:var(--green)}
.footer{position:absolute;left:0;bottom:0;width:476px;height:23px;background:var(--navy);
  color:#fff;display:flex;align-items:center;justify-content:center}
.footer--url{font-weight:700;font-size:12px}
.footer--quote{font-style:italic;font-size:9.5px}

/* right page */
.services-title{position:absolute;left:0;top:0;width:476px;height:27px;
  background:linear-gradient(90deg,var(--navy) 0%,var(--blue) 45%,var(--green) 100%);
  color:#fff;font-style:italic;font-size:22px;letter-spacing:1px;padding:2px 0 0 10px}
.services-intro{position:absolute;left:12px;top:32px;width:322px;font-size:9px;line-height:18px}
.services-intro .ticks li{margin-bottom:0;line-height:18px}
.photo--student-desk{left:328px;top:27px;width:148px;height:120px;
  background:linear-gradient(135deg,#e9e4dd 0%,#b98d6a 50%,#5b3b2a 100%)}
.section-head{position:absolute;height:24px;
  background:linear-gradient(90deg,#dfe7ee 0%,var(--light-green) 100%);
  font-weight:700;font-size:11.5px;color:var(--navy);padding:5px 0 0 6px}
.section-text{position:absolute;font-size:7.6px;line-height:15px}
.section-text--college{line-height:14.5px}
.section-text--transfer{line-height:13px}
.section-text--scholarships{line-height:14px}
.photo--two-girls{left:0;top:222px;width:155px;height:138px;
  background:linear-gradient(135deg,#f4efe8 0%,#d7b08a 45%,#8a5a3c 100%)}
.photo--smiling-student{left:326px;top:361px;width:150px;height:163px;
  background:linear-gradient(135deg,#e8e3dc 0%,#b9876a 45%,#45322a 100%)}
.photo--graduate{left:0;top:600px;width:120px;height:133px;
  background:linear-gradient(180deg,#f3f3f3 0%,#3a3230 45%,#1c1c1c 100%)}
</style>
</head>
<body>

<section class="page page--left">
  <div class="who-block">WHO<br>WE<br>ARE</div>
  <div class="photo photo--students" role="img" aria-label="Group of students studying together at a table"></div>

  <div class="intro">
    <p>Our mission is to make quality education accessible and affordable to the families we serve.</p>
    <p>Our services are designed with the child's future in mind. Whether one is seeking an academic or non-academic environment, it is important to us that we set our clients up for success.</p>
    <ul class="ticks">
      <li><svg viewBox="0 0 10 10"><path d="M1 5 L4 8 L9 1" fill="none" stroke="var(--tick)" stroke-width="1.6"/></svg>We are a family-centered organization and our goals are the same as those of our clients; for their child to thrive and reach their goals and dreams.</li>
      <li><svg viewBox="0 0 10 10"><path d="M1 5 L4 8 L9 1" fill="none" stroke="var(--tick)" stroke-width="1.6"/></svg>With over 10 years of experience in the business, we are aware of the financial obstacles created by the ever increasing cost in education.</li>
      <li><svg viewBox="0 0 10 10"><path d="M1 5 L4 8 L9 1" fill="none" stroke="var(--tick)" stroke-width="1.6"/></svg>Our expert consultants work closely with families to map out their educational budget and find the best affordable and quality educational options.</li>
    </ul>
  </div>

  <div class="photo photo--library" role="img" aria-label="Curved library interior lined with bookshelves"></div>
  <div class="library-banner">LANDING YOU IN THE RIGHT INSTITUTE ACROSS USA AND CANADA</div>

  <div class="brand"><span class="brand-dot"></span>Plorva</div>

  <div class="footer footer--url">http://plorvaeducationalconsultants.example/</div>
</section>

<section class="page page--right">
  <div class="services-title">OUR SERVICES</div>

  <div class="services-intro">
    <p>Finding the right school or program for your child is one of the most important decisions your family will make. The right choice will make a major impact on your child's future.</p>
    <p>Our package includes :</p>
    <ul class="ticks">
      <li><svg viewBox="0 0 10 10"><path d="M1 5 L4 8 L9 1" fill="none" stroke="var(--tick)" stroke-width="1.6"/></svg>Intake interview</li>
      <li><svg viewBox="0 0 10 10"><path d="M1 5 L4 8 L9 1" fill="none" stroke="var(--tick)" stroke-width="1.6"/></svg>Present range of options based on needs and goals of the family</li>
      <li><svg viewBox="0 0 10 10"><path d="M1 5 L4 8 L9 1" fill="none" stroke="var(--tick)" stroke-width="1.6"/></svg>Interview coaching</li>
      <li><svg viewBox="0 0 10 10"><path d="M1 5 L4 8 L9 1" fill="none" stroke="var(--tick)" stroke-width="1.6"/></svg>Assistance with application and essays</li>
      <li><svg viewBox="0 0 10 10"><path d="M1 5 L4 8 L9 1" fill="none" stroke="var(--tick)" stroke-width="1.6"/></svg>Updates on student progress throughout their enrollment with the school</li>
      <li><svg viewBox="0 0 10 10"><path d="M1 5 L4 8 L9 1" fill="none" stroke="var(--tick)" stroke-width="1.6"/></svg>Advisement on financial documents and visa applications</li>
    </ul>
  </div>
  <div class="photo photo--student-desk" role="img" aria-label="Student smiling at a computer desk in a classroom"></div>

  <div class="photo photo--two-girls" role="img" aria-label="Two students smiling with notebooks"></div>
  <div class="section-head" style="left:165px;top:225px;width:311px">Boarding schools:</div>
  <p class="section-text" style="left:165px;top:254px;width:302px">Students who want the best out of their grade school experience are likely to choose boarding schools because they are proven to better prepare students for university. North American boarding schools provide a quality dynamic experience that will facilitate personal growth in independence, leadership, and confidence as well as provide the academic curriculum necessary to prepare students for university.</p>

  <div class="section-head" style="left:0;top:363px;width:310px">College Admission:</div>
  <p class="section-text section-text--college" style="left:12px;top:393px;width:308px">As Educational Consultants, we specialize in college/university admissions and we understand how confusing, time-consuming, and stressful the application process can be. Our experienced counselors are here to answer your questions and guide you step by step. As Parents and students may have limited access to information on schools, may not know or understand the entire process as a whole, nor where/how to begin, our experts counselors have a solutions. Clients increase the odds of admissions with our comprehensive plan of action. We believe that regardless of a student's level of involvement in extra-curricular activities or preparedness, they still possess something they can offer to the university; therefore we help them shine on their college applications.</p>
  <div class="photo photo--smiling-student" role="img" aria-label="Student resting chin on hand with classmates behind"></div>

  <div class="section-head" style="left:0;top:544px;width:320px">Transfer students:</div>
  <p class="section-text section-text--transfer" style="left:12px;top:571px;width:456px">Need to find a school an alternative school that is a better match for you? We work with students and families to transfer from one school to another.</p>

  <div class="photo photo--graduate" role="img" aria-label="Graduate in cap and gown holding a diploma"></div>
  <div class="section-head" style="left:125px;top:604px;width:351px">Scholarships:</div>
  <p class="section-text section-text--scholarships" style="left:134px;top:632px;width:335px">Funding the education for your children in some of the world's top schools can be very expensive as tuition and fees increase at an average of 4% every year. We work with you to determine the budget for your family, applying to scholarship available and guide you through the financial aid process.<br>Over 70% of our clients have been awarded scholarships or Financial Aid, making your education goals attainable an affordable and your children education possible.</p>

  <div class="footer footer--quote">"Our consultants are members of CEAN, the leading association for educational consultants in North America."</div>
</section>

</body>
</html>
```